Locksmith Business Cards

My father-in-law is in need of new business cards for his locksmith business and I need to impress him. Kindly help me out!

You can see the previous business card attached. It is a family run business in North Wales.

No individual names on the cards.

Key Things to Feature:
- The words "Prompt", "Local", "Reliable" (as you can see under the logo on the website)
- 24h Emergency Service
- Covering All of North Wales, the Wirral and Chester
- The color blue
- A key or a lock would be interesting (similar to the ones that come up when you google locksmith business card)

Optional (only if design includes bullet points, like the example below):
https://imgvaultcdnx.net/design_img/318264/57190/57190_2749031_318264_image.jpg
- Residential / Commercial / Automotive
- Alarms & Cameras
- Key Cutting & Safes

https://www.bryncoed-locksmiths-demo.co.uk/

Locksmith

01632 960 418
07700 900 362
bryncoedlocksmiths@mailvalex.com
Bryncoed Locksmiths, Hafod Barn, 4 Pennant Rd., Llandudno LL39 7QZ
www.bryncoed-locksmiths-demo.co.uk

• - The words "Prompt", "Local", "Reliable" (as you can see under the logo on the website)
• - 24h Emergency Service
• - Covering All of North Wales, the Wirral and Chester
• - A key or a lock would be interesting (similar to the ones that come up when you google locksmith business card)

```html
<!DOCTYPE html>
<html lang="en">
<head>
<meta charset="utf-8">
<title>Bryncoed Locksmiths – Business Cards</title>
<link href="https://fonts.googleapis.com/css2?family=Roboto+Condensed:wght@400;700&family=Roboto:wght@400;500&display=swap" rel="stylesheet">
<style>
  :root {
    --navy: #262a78;
    --navy-deep: #1d2163;
    --blue-mid: #4a57a8;
    --blue-light: #6f7cc4;
    --silver: #a9abb3;
    --ink: #2e3282;
    --grey-text: #5c5f74;
    --paper: #ffffff;
    --backdrop: #e9eaee;
  }
  * { box-sizing: border-box; margin: 0; padding: 0; }
  html, body { width: 1200px; height: 896px; overflow: hidden; }
  body {
    background: var(--backdrop);
    font-family: "Roboto", Arial, sans-serif;
    display: flex;
    flex-direction: column;
    align-items: center;
    justify-content: center;
    gap: 36px;
  }
  .card {
    position: relative;
    width: 680px;
    height: 390px;
    border-radius: 22px;
    overflow: hidden;
    box-shadow: 0 8px 24px rgba(20, 24, 60, 0.18);
  }

  .brand { display: flex; align-items: center; gap: 14px; }
  .brand__mark { width: 40px; height: 40px; flex: none; }
  .brand__name {
    font-family: "Roboto Condensed", Arial, sans-serif;
    font-weight: 700;
    text-transform: uppercase;
    line-height: 1;
    letter-spacing: 0.5px;
    white-space: nowrap;
  }

  /* Front */
  .card--front {
    background: linear-gradient(135deg, #2d3284 0%, var(--navy) 55%, var(--navy-deep) 100%);
    color: var(--paper);
  }
  .card--front .brand { position: absolute; left: 48px; top: 52px; }
  .card--front .brand__mark { background: var(--paper); }
  .card--front .brand__name { font-size: 34px; color: var(--paper); }
  .front__headline {
    position: absolute; left: 48px; top: 116px;
    font-family: "Roboto Condensed", Arial, sans-serif;
    font-size: 26px; font-weight: 400;
  }
  .services {
    position: absolute; left: 72px; top: 164px;
    list-style: none;
    font-family: "Roboto Condensed", Arial, sans-serif;
    font-size: 21px; line-height: 31px;
  }
  .services li { position: relative; padding-left: 24px; }
  .services li::before {
    content: ""; position: absolute; left: 0; top: 11px;
    width: 9px; height: 9px; border-radius: 50%; background: var(--paper);
  }
  .coverage {
    position: absolute; left: 48px; bottom: 30px;
    font-family: "Roboto Condensed", Arial, sans-serif;
    font-size: 17px; color: var(--paper); opacity: 0.9;
  }

  /* Back */
  .card--back { background: var(--paper); }
  .card--back .brand { position: absolute; left: 40px; top: 44px; }
  .card--back .brand__mark { background: var(--ink); }
  .card--back .brand__name { font-size: 32px; color: var(--ink); }
  .tagline {
    position: absolute; left: 94px; top: 86px;
    font-family: "Roboto Condensed", Arial, sans-serif;
    font-size: 17px; color: var(--grey-text);
  }
  .contact-rule {
    position: absolute; left: 40px; top: 236px;
    width: 260px; height: 1px; background: var(--blue-mid);
  }
  .contacts {
    position: absolute; left: 40px; top: 248px;
    list-style: none;
    font-size: 13.5px; line-height: 21px; color: var(--grey-text);
  }
  .contacts li { display: flex; align-items: center; gap: 9px; }
  .contacts svg { width: 12px; height: 12px; flex: none; }
  .swoosh { position: absolute; inset: 0; width: 680px; height: 390px; }
  .address {
    font-family: "Roboto Condensed", Arial, sans-serif;
    font-size: 13px; fill: var(--paper);
  }
</style>
</head>
<body>

  <section class="card card--front" aria-label="Card front">
    <div class="brand">
      <span class="brand__mark"></span>
      <span class="brand__name">Bryncoed Locksmiths</span>
    </div>
    <p class="front__headline">24h Emergency Service</p>
    <ul class="services">
      <li>Residential</li>
      <li>Commercial</li>
      <li>Automotive</li>
      <li>Alarms &amp; Cameras</li>
      <li>Key Cutting &amp; Safes</li>
    </ul>
    <p class="coverage">Covering All of North Wales, the Wirral and Chester</p>
  </section>

  <section class="card card--back" aria-label="Card back">
    <svg class="swoosh" viewBox="0 0 680 390" aria-hidden="true">
      <path d="M680,104 C590,118 540,220 390,292 C290,340 190,368 60,390 L680,390 Z" fill="var(--blue-light)"/>
      <path d="M680,118 C596,132 546,232 396,302 C296,348 200,372 100,390 L680,390 Z" fill="var(--paper)"/>
      <path d="M680,128 C600,142 548,240 398,306 C298,350 206,374 120,390 L680,390 Z" fill="var(--silver)"/>
      <path d="M680,150 C600,165 540,250 400,310 C300,352 220,372 150,390 L680,390 Z" fill="var(--navy)"/>
      <text class="address" x="662" y="334" text-anchor="end">Bryncoed Locksmiths,</text>
      <text class="address" x="662" y="356" text-anchor="end">Hafod Barn, 4 Pennant Rd., Llandudno LL39 7QZ</text>
    </svg>

    <div class="brand">
      <span class="brand__mark"></span>
      <span class="brand__name">Bryncoed Locksmiths</span>
    </div>
    <p class="tagline">Prompt. Local. Reliable</p>

    <div class="contact-rule"></div>
    <ul class="contacts">
      <li>
        <svg viewBox="0 0 12 12" aria-hidden="true"><path d="M2.5 1 L4.5 1 L5.2 3.6 L4 4.6 C4.6 6 6 7.4 7.4 8 L8.4 6.8 L11 7.5 L11 9.5 C11 10.3 10.3 11 9.5 11 C5 11 1 7 1 2.5 C1 1.7 1.7 1 2.5 1 Z" fill="var(--grey-text)"/></svg>
        01632 960 418
      </li>
      <li>
        <svg viewBox="0 0 12 12" aria-hidden="true"><rect x="3" y="0.8" width="6" height="10.4" rx="1" fill="none" stroke="var(--grey-text)" stroke-width="1.2"/><circle cx="6" cy="9.2" r="0.7" fill="var(--grey-text)"/></svg>
        07700 900 362
      </li>
      <li>
        <svg viewBox="0 0 12 12" aria-hidden="true"><rect x="0.8" y="2.2" width="10.4" height="7.6" fill="none" stroke="var(--grey-text)" stroke-width="1.2"/><path d="M1 2.6 L6 6.6 L11 2.6" fill="none" stroke="var(--grey-text)" stroke-width="1.2"/></svg>
        bryncoedlocksmiths@mailvalex.com
      </li>
      <li>
        <svg viewBox="0 0 12 12" aria-hidden="true"><circle cx="6" cy="6" r="5" fill="none" stroke="var(--grey-text)" stroke-width="1.1"/><ellipse cx="6" cy="6" rx="2.2" ry="5" fill="none" stroke="var(--grey-text)" stroke-width="0.9"/><path d="M1 6 H11" stroke="var(--grey-text)" stroke-width="0.9"/></svg>
        www.bryncoed-locksmiths-demo.co.uk
      </li>
    </ul>
  </section>

</body>
</html>
```